Brasko Construction Business Card

I need a business card design for my company.
We are a construction/machinery company.
I would like to see my logo on the front of the card and my details on the other side
I would like the card to be black or dark grey in colour,with my logo as i send it or modified with a lighter blue colour
I would like to see the design kept fairly simple,but eye catching at the same time
Industry/Entity Type
Business
Contact Information for Business Card
Name
Phone Number
Address
Email
Colors
00a990
1b1b1b
000000
474747
ececec

```html
<!DOCTYPE html>
<html lang="en">
<head>
<meta charset="utf-8">
<title>Brasko Construction Business Card</title>
<link rel="stylesheet" href="https://fonts.googleapis.com/css2?family=Roboto:wght@400;500;700&display=swap">
<style>
  :root {
    --teal: #00a990;
    --ink: #1b1b1b;
    --black: #000000;
    --slate: #474747;
    --paper: #ececec;
    --card: #f7f7f7;
    --backdrop: #d9d9d9;
  }
  * { margin: 0; padding: 0; box-sizing: border-box; }
  html, body {
    width: 1200px; height: 716px; overflow: hidden;
    background: var(--backdrop);
    font-family: "Roboto", Arial, sans-serif;
  }
  .canvas { position: relative; width: 1200px; height: 716px; }
  .card {
    position: absolute; top: 208px;
    width: 525px; height: 300px;
    background: var(--card);
    box-shadow: 0 6px 0 var(--ink), 0 12px 24px rgba(0,0,0,.25);
    overflow: hidden;
  }
  .card-front { left: 45px; }
  .card-back { left: 630px; }

  .brand { display: flex; align-items: center; gap: 12px; color: var(--ink); font-weight: 700; }
  .brand-square { width: 22px; height: 22px; background: var(--ink); flex: none; }
  .brand-name { text-transform: uppercase; letter-spacing: 1px; line-height: 1; }

  .card-front .brand { position: absolute; left: 0; right: 0; top: 128px; justify-content: center; }
  .card-front .brand-name { font-size: 30px; }

  .card-back .brand { position: absolute; left: 36px; top: 42px; }
  .card-back .brand-name { font-size: 24px; }
  .divider { position: absolute; left: 300px; top: 36px; width: 1px; height: 52px; background: var(--teal); display: none; }

  .holder { position: absolute; left: 36px; top: 112px; }
  .holder-name { color: var(--teal); font-weight: 700; font-size: 17px; }
  .holder-role { color: var(--slate); font-size: 11px; margin-top: 3px; }

  .contact { position: absolute; left: 256px; top: 168px; list-style: none; color: var(--ink); font-size: 13px; }
  .contact li { display: flex; align-items: center; gap: 8px; height: 19px; }
  .contact svg { width: 11px; height: 11px; fill: var(--teal); flex: none; }
  .contact .address { padding-left: 0; margin-top: 2px; }

  .band { position: absolute; left: 0; bottom: 0; width: 525px; height: 26px; }
</style>
</head>
<body>
<main class="canvas">
  <section class="card card-front" aria-label="Card front">
    <div class="brand">
      <span class="brand-square"></span>
      <span class="brand-name">Brasko Construction</span>
    </div>
  </section>

  <section class="card card-back" aria-label="Card back">
    <div class="brand">
      <span class="brand-square"></span>
      <span class="brand-name">Brasko Construction</span>
    </div>

    <div class="holder">
      <p class="holder-name">Your Good Name</p>
      <p class="holder-role">General Contractor</p>
    </div>

    <ul class="contact">
      <li>
        <svg viewBox="0 0 24 24" aria-hidden="true"><path d="M6.6 10.8a15.1 15.1 0 0 0 6.6 6.6l2.2-2.2a1 1 0 0 1 1-.25 11.4 11.4 0 0 0 3.6.57 1 1 0 0 1 1 1V20a1 1 0 0 1-1 1A17 17 0 0 1 3 4a1 1 0 0 1 1-1h3.5a1 1 0 0 1 1 1c0 1.25.2 2.45.57 3.57a1 1 0 0 1-.25 1z"/></svg>
        <span>+00 111 222 3333</span>
      </li>
      <li>
        <svg viewBox="0 0 24 24" aria-hidden="true"><path d="M2 5h20v14H2z M3 6l9 7 9-7" /></svg>
        <span>www.yourwebsite.com</span>
      </li>
      <li>
        <svg viewBox="0 0 24 24" aria-hidden="true"><circle cx="12" cy="12" r="10"/></svg>
        <span>yourname@yourwebsite.com</span>
      </li>
      <li class="address"><span>Your Long Commercial address, Code</span></li>
    </ul>

    <svg class="band" viewBox="0 0 525 26" preserveAspectRatio="none" aria-hidden="true">
      <polygon points="0,14 320,14 340,26 0,26" fill="var(--slate)"/>
      <polygon points="310,14 525,0 525,26 330,26" fill="var(--teal)"/>
    </svg>
  </section>
</main>
</body>
</html>
```